Re-Design of Business Card for Marine Sales People

We are looking to Re-design our business cards to look like they are in the 21st century. We are a full service marina and sell a lot of new/used boats. May want a spot on the card for our 3 main brands we sell. A picture spot of the sales man would be nice, but not necessarily.

```html
<!DOCTYPE html>
<html lang="en">
<head>
<meta charset="utf-8">
<title>Bayhollow Marine – Business Cards</title>
<link href="https://fonts.googleapis.com/css2?family=Questrial&display=swap" rel="stylesheet">
<style>
  :root {
    --backdrop: #2e2f31;
    --card: #ffffff;
    --card-shade: #eceef0;
    --wave-blue: #1a98d5;
    --wave-light: #5bb8e6;
    --navy: #1b2b4b;
    --ink: #4a4a4a;
  }
  * { margin: 0; padding: 0; box-sizing: border-box; }
  html, body { width: 1200px; height: 900px; overflow: hidden; }
  body {
    background: var(--backdrop);
    font-family: "Questrial", "Century Gothic", sans-serif;
    position: relative;
  }
  .card {
    position: absolute;
    left: 285px;
    width: 630px;
    height: 360px;
    background: linear-gradient(135deg, var(--card) 40%, var(--card-shade));
    overflow: hidden;
    box-shadow: 0 10px 30px rgba(0,0,0,.45);
  }
  .card--front { top: 60px; }
  .card--back { top: 480px; }
  .card__wave { position: absolute; inset: 0; width: 100%; height: 100%; }
  .brand-name {
    position: absolute;
    color: var(--navy);
    font-size: 34px;
    letter-spacing: 3px;
    white-space: nowrap;
  }
  .card--front .brand-name { left: 190px; top: 120px; }
  .card--back .brand-name { left: 170px; top: 50px; }
  .web-address {
    position: absolute;
    color: var(--navy);
    font-size: 17px;
    letter-spacing: .5px;
    transform: rotate(-13deg);
    transform-origin: left center;
    white-space: nowrap;
  }
  .card--front .web-address { left: 270px; top: 312px; }
  .card--back .web-address { left: 300px; top: 322px; }
  .contact {
    position: absolute;
    color: var(--ink);
    font-size: 15px;
    font-style: normal;
    line-height: 1.45;
  }
  .contact--left { left: 56px; top: 190px; }
  .contact--right { right: 50px; top: 108px; text-align: right; }
  .contact__line { display: flex; align-items: center; gap: 7px; }
  .contact--right .contact__line { justify-content: flex-end; }
  .contact__indent { padding-left: 19px; }
  .contact--right .contact__indent { padding-left: 0; padding-right: 19px; }
  .icon { width: 12px; height: 12px; flex: none; fill: var(--wave-blue); }
</style>
</head>
<body>

<section class="card card--front" aria-label="Card front">
  <svg class="card__wave" viewBox="0 0 630 360" preserveAspectRatio="none" aria-hidden="true">
    <path d="M0,338 C130,330 190,262 300,262 C410,262 470,190 630,170 L630,360 L0,360 Z" fill="var(--wave-blue)"/>
    <path d="M0,322 C120,318 180,256 290,250 C400,244 460,176 630,158" fill="none" stroke="var(--wave-light)" stroke-width="4"/>
    <path d="M0,312 C110,306 170,250 280,240 C390,230 460,168 630,150" fill="none" stroke="var(--wave-blue)" stroke-width="2"/>
  </svg>
  <div class="brand-name">BAYHOLLOW MARINE</div>
  <div class="web-address">www.bayhollowmarine.com</div>
</section>

<section class="card card--back" aria-label="Card back">
  <svg class="card__wave" viewBox="0 0 630 360" preserveAspectRatio="none" aria-hidden="true">
    <path d="M0,345 C130,338 200,290 310,286 C420,282 480,228 630,210 L630,360 L0,360 Z" fill="var(--wave-blue)"/>
    <path d="M0,330 C120,326 190,280 300,274 C410,268 470,216 630,198" fill="none" stroke="var(--wave-light)" stroke-width="4"/>
    <path d="M0,320 C110,314 180,272 290,264 C400,256 470,208 630,190" fill="none" stroke="var(--wave-blue)" stroke-width="2"/>
  </svg>
  <div class="brand-name">BAYHOLLOW MARINE</div>

  <address class="contact contact--left">
    <div class="contact__line">
      <svg class="icon" viewBox="0 0 24 24" aria-hidden="true"><path d="M6.6 10.8a15.1 15.1 0 0 0 6.6 6.6l2.2-2.2c.3-.3.7-.4 1-.2 1.1.4 2.3.6 3.6.6.6 0 1 .4 1 1V20c0 .6-.4 1-1 1C10.6 21 3 13.4 3 4c0-.6.4-1 1-1h3.5c.6 0 1 .4 1 1 0 1.3.2 2.5.6 3.6.1.3 0 .7-.2 1z"/></svg>
      (555) 214-7730
    </div>
    <div class="contact__line">
      <svg class="icon" viewBox="0 0 24 24" aria-hidden="true"><path d="M12 2a7 7 0 0 0-7 7c0 5.2 7 13 7 13s7-7.8 7-13a7 7 0 0 0-7-7zm0 9.5A2.5 2.5 0 1 1 12 6.5a2.5 2.5 0 0 1 0 5z"/></svg>
      48 Harbor Road.
    </div>
    <div class="contact__indent">Millbrook, NH 03101</div>
  </address>

  <address class="contact contact--right">
    <div class="contact__line">
      (555) 309-6152
      <svg class="icon" viewBox="0 0 24 24" aria-hidden="true"><path d="M6.6 10.8a15.1 15.1 0 0 0 6.6 6.6l2.2-2.2c.3-.3.7-.4 1-.2 1.1.4 2.3.6 3.6.6.6 0 1 .4 1 1V20c0 .6-.4 1-1 1C10.6 21 3 13.4 3 4c0-.6.4-1 1-1h3.5c.6 0 1 .4 1 1 0 1.3.2 2.5.6 3.6.1.3 0 .7-.2 1z"/></svg>
    </div>
    <div class="contact__line">
      17 Cove Ln.
      <svg class="icon" viewBox="0 0 24 24" aria-hidden="true"><path d="M12 2a7 7 0 0 0-7 7c0 5.2 7 13 7 13s7-7.8 7-13a7 7 0 0 0-7-7zm0 9.5A2.5 2.5 0 1 1 12 6.5a2.5 2.5 0 0 1 0 5z"/></svg>
    </div>
    <div class="contact__indent">Fairhaven, NH 03102</div>
  </address>

  <div class="web-address">www.bayhollowmarine.com</div>
</section>

</body>
</html>
```